Stationary Set and Logo Update **PAYMENT GUARANTEED**

Stationery Design and Logo Update

About Us

Trindex Supply is a wholesale distributor of OEM [original brand] and compatible [generic brand] parts and supplies for use in copiers, faxes, printers, and multi-function machines. In plain English…we sell all the parts and supplies [such as toner] that make up any office equipment which outputs an image on paper.

Trindex was the 1st distributor to develop and sell a generic brand copier part in the United States. We have been in business since 1972 [nearly 40 years]. Our tagline is "The Steady Choice," as in our company was the first alternative product that copier dealers had to buying original brand copier parts. Trindex is known for offering reliable and cost-effective OEM and compatible products.

Project

We require a fresh, modern and corporate identity. Please submit a stationary package inclusive of a double-sided business card (2" x 3.5"), letterhead (8.5'x11"), and standard #10 envelope (4-1/8” x 9-1/2). You may use our current logo or preferably your take on an updated one. If an attempt is made in updating the logo #004D8E or a similar hue should be used as the primary color.

The design should be clean, simple, modern and professional and make an immediate impact.

Target Market(s)

Copier and printer dealers who lease and service imaging equipment in the United States and Latin America.

Industry/Entity Type

Business

Requirements
Must have
• Simple, clean, modern and professional. Please use #004D8E or a similar hue as the primary color. Letterhead must accommate (2) addresses. We have 2 locations.
Nice to have
• A simple, modern update to our current logo. https://assets.mailvorbo.example/fs030/5520384417702/img/418.jpg
Should not have
• More than (2) colors on logo.

```html
<!DOCTYPE html>
<html lang="en">
<head>
<meta charset="utf-8">
<title>Trindex Supply – #10 Envelope</title>
<link rel="stylesheet" href="https://fonts.googleapis.com/css2?family=Source+Sans+3:wght@400;600;700&display=swap">
<style>
  :root {
    --brand-blue: #004d8e;
    --accent-green: #97b31f;
    --paper: #ffffff;
    --ink-grey: #6b6f74;
    --rule-blue: #1f5d9c;
    --receiver-gold: #e09a2a;
    --sq-1: #0a4f8e;
    --sq-10: #2d9cf2;
  }
  * { box-sizing: border-box; margin: 0; padding: 0; }
  html, body {
    width: 1200px;
    height: 510px;
    overflow: hidden;
    background: #ffffff;
    font-family: "Source Sans 3", "Myriad Pro", sans-serif;
  }
  .envelope {
    position: absolute;
    left: 30px;
    top: 6px;
    width: 1140px;
    height: 492px;
    background: var(--brand-blue);
    box-shadow: 2px 3px 6px rgba(0,0,0,0.35);
    overflow: hidden;
  }
  .envelope__accent {
    position: absolute;
    left: 44px;
    top: 40px;
    right: 0;
    bottom: 0;
    background: var(--accent-green);
    border-top-left-radius: 132px;
  }
  .envelope__face {
    position: absolute;
    left: 54px;
    top: 50px;
    right: 0;
    bottom: 0;
    background: var(--paper);
    border-top-left-radius: 122px;
  }
  .tile-strip {
    position: absolute;
    top: 10px;
    right: 14px;
    display: flex;
    gap: 13px;
  }
  .tile-strip span {
    width: 20px;
    height: 20px;
    display: block;
  }
  .sender {
    position: absolute;
    left: 98px;
    top: 94px;
  }
  .sender__brand {
    display: flex;
    align-items: center;
    gap: 10px;
    color: var(--brand-blue);
    font-weight: 700;
    font-size: 46px;
    line-height: 1;
    letter-spacing: -0.5px;
  }
  .sender__mark {
    width: 36px;
    height: 36px;
    border-radius: 50%;
    background: var(--brand-blue);
  }
  .sender__details {
    list-style: none;
    margin-top: 14px;
    color: var(--ink-grey);
    font-size: 14.5px;
    line-height: 26px;
  }
  .recipient {
    position: absolute;
    left: 535px;
    top: 206px;
  }
  .recipient__label {
    color: var(--receiver-gold);
    font-size: 34px;
    font-weight: 400;
    line-height: 40px;
  }
  .recipient__line {
    display: block;
    height: 0;
    border-top: 1.5px solid var(--rule-blue);
    margin-top: 35px;
  }
  .recipient__line:first-of-type { margin-top: 28px; }
  .footer {
    position: absolute;
    left: 68px;
    right: 24px;
    top: 456px;
    border-top: 1.2px solid var(--rule-blue);
    display: flex;
    justify-content: space-between;
    align-items: baseline;
    padding: 7px 0 0 6px;
    color: var(--ink-grey);
  }
  .footer__address { font-size: 18px; }
  .footer__contact {
    font-size: 15px;
    display: flex;
    gap: 20px;
  }
</style>
</head>
<body>
  <div class="envelope">
    <div class="envelope__accent"></div>
    <div class="envelope__face"></div>

    <div class="tile-strip" aria-hidden="true">
      <span style="background:#08508f"></span>
      <span style="background:#0a5598"></span>
      <span style="background:#0d5ca3"></span>
      <span style="background:#1064b0"></span>
      <span style="background:#146dbd"></span>
      <span style="background:#1876ca"></span>
      <span style="background:#1d80d6"></span>
      <span style="background:#2289e1"></span>
      <span style="background:#2793ea"></span>
      <span style="background:#2d9cf2"></span>
    </div>

    <div class="sender">
      <div class="sender__brand"><span class="sender__mark"></span>Trindex</div>
      <ul class="sender__details">
        <li>Address Line - 1</li>
        <li>Email: 123@trindexmail.example</li>
        <li>Phone: 000 - 000 - 0000</li>
        <li>www.assets.mailvorbo.example</li>
      </ul>
    </div>

    <div class="recipient">
      <p class="recipient__label">Receiver Name</p>
      <span class="recipient__line" style="width:450px"></span>
      <span class="recipient__line" style="width:422px"></span>
      <span class="recipient__line" style="width:376px"></span>
      <span class="recipient__line" style="width:324px"></span>
    </div>

    <div class="footer">
      <span class="footer__address">Address Line - 2</span>
      <span class="footer__contact">
        <span>Phone: 000 - 000 - 0000</span>
        <span>Email: 123@trindexmail.example</span>
        <span>www.assets.mailvorbo.example</span>
      </span>
    </div>
  </div>
</body>
</html>
```